New word press website site design

We provide email marketing to aircraft brokers and dealers to assist in finding buyers for their aircraft.

Our target market to purchase our broadcasts are the aircraft sellers – NOT the buyers.

Our target market when sending the email broadcast, are the buyers (end users).

The website should target brokers and our email database targets the buyers.

We do not buy or sell aircraft as a company. We provide email marketing solutions to connect buyers and sellers of aircraft.

Our other site is vesseltrove.net and will be redesigned soon. Please use it as a reference as far as general scope but they layout can be completely different and should include helicopters only as far as imagery. The colors should be similar as the logos are similar, however we do NOT want both sites to be identical in use of primary color

Plenty of images and sample broadcasts attached to use as needed throughout the site.

Headlines listed below with some text copy.

In the event that we need to add more text, please use standard greek text as a place holder for the purposes of the mockup design.

Need to have a “SUBSCRIBE” button to join our mailing list.

Possible Headlines:

Exclusively Showcasing Rotor Wing Aircraft to the Global Marketplace

Showcasing Pre-Owned Helicopters Available For Sale, Lease, Trade, or Wanted for Acquisition.

Mobile-optimized Email Campaigns that Render Correctly Across all Devices

Targeted worldwide recipients that currently own, operate, or have an interest in rotor wing aircraft

STRONGEST Rotor Wing Database in the Industry

Text/Copy:

HOME
Rotorline Parade is one of most powerful marketing tools in the industry to utilize in reaching targeted buyers of pre-owned helicopters. Rotorline Parade provides the rotor wing aircraft market with a fast, effective, and affordable email broadcast solution to utilize in the marketing of Helicopters for sale.

Developed Exclusively to Parade Rotor Wing Aircraft to the Global marketplace, Rotorline Parade is a powerful tool designed to maximize leads and accelerate the sales process by providing the ability to reach a global network of Helicopter buyers in a matter of seconds.

DATABASE:

While Rotorline Parade is delivered to all known broker/dealers, our primary focus is in reaching end users. Our opt-in/opt-out recipient database is updated daily and developed specifically to deliver the latest details on helicopters available for sale or lease to the inboxes of a global network of Helicopter buyers and sellers.

· Helicopter Owners

· Helicopter Operators

· Helicopter Charter Services

· Helicopter Management Companies

· Corporate/Municipal Flight Departments

· Helicopter Pilots

· Senior Aviation Executives

· Wealth Management Firms

· High Net Worth Individuals

· Helicopter Broker/Dealers

Helicopter Tour/Travel Firms

· Off Shore Oil & Gas Production Firms

· Municipalities/Media/Medevac Firms

Our recipient database is continuously updated and developed specifically to reach buyers and sellers of Helicopters. This ensures that your Helicopter will be showcased to the right people. Rotorline Parade does not broadcast non-rotor wing aircraft and focuses exclusively on the Global Helicopter Market.

Broadcast Design:

Rotorline Parade broadcast ads are custom designed for you by incorporating your corporate image and branding. Because you have worked hard in developing your corporate image, we strive to maintain it while designing an ad that will showcase your Helicopter to its best advantage. Rotorline Parade utilizes Mobile-optimized Email Campaigns with Responsive Coding to render correctly across all devices

Once you have approved the design, we schedule the broadcast to be sent on the available date and time you request. The broadcast will link to your website and the results can be immediate. All email leads and replies will go to the email address that you provided.

Pricing:
Create a place holder for 3 Different Broadcast Packages

-Broadcast Package A
-Broadcast Package B
-Broadcast Package C

Target Market(s)

The target market is any person or company that has aircraft for sale. We work with brokers, dealers, and owners to assist in finding buyers for their aircraft using email marketing campaigns (Parade broadcasts).

Industry/Entity Type

Aviation

Colors
0255a3
00a990

Requirements
Nice to have
• Samples of helicopter for sale broadcast ads in /image gallery/slider

```html
<!DOCTYPE html>
<html lang="en">
<head>
<meta charset="utf-8">
<title>Rotorline Parade</title>
<link href="https://fonts.googleapis.com/css2?family=Poppins:wght@400;500;600&family=Open+Sans:wght@400;600&display=swap" rel="stylesheet">
<style>
:root{
  --green:#5cb31a;
  --green-dark:#3f8f12;
  --navy:#0f2a4b;
  --navy-deep:#0a1a31;
  --navy-btn:#17396a;
  --ink:#1d1d1d;
  --body:#5a5a5a;
  --white:#ffffff;
  --grey-band:#ececec;
}
*{margin:0;padding:0;box-sizing:border-box}
html,body{width:1200px;height:2853px;overflow:hidden}
body{position:relative;background:var(--white);font-family:"Open Sans",Arial,sans-serif;color:var(--body)}
h1,h2,h3,h4,.nav,.btn{font-family:"Poppins",Arial,sans-serif}
.abs{position:absolute}

/* Header / hero */
.hero{position:absolute;left:0;top:0;width:1200px;height:512px;overflow:hidden}
.hero svg.hero-bg{position:absolute;left:0;top:0}
.logo{left:219px;top:26px;font-family:"Poppins",sans-serif;font-weight:600;font-size:20px;color:var(--white);display:flex;align-items:center;gap:8px;white-space:nowrap}
.logo .dot{width:12px;height:12px;border-radius:50%;background:var(--green)}
.nav{left:445px;top:32px;display:flex;gap:15px;font-size:11px;font-weight:500;color:var(--white);white-space:nowrap}
.nav a{color:var(--white);text-decoration:none;padding-bottom:6px}
.nav a.active{border-bottom:2px solid var(--green)}
.phone{left:800px;top:32px;font-family:"Poppins",sans-serif;font-size:11.5px;color:var(--white);display:flex;align-items:center;gap:7px;white-space:nowrap}
.btn-subscribe{left:898px;top:27px;width:82px;height:29px;background:var(--green);color:var(--white);font-size:11px;font-weight:600;display:flex;align-items:center;justify-content:center;letter-spacing:.3px}
.hero-title{left:614px;top:172px;width:345px;font-size:27px;line-height:31px;font-weight:600;color:var(--white)}
.btn-outline{left:614px;top:289px;width:132px;height:26px;border:1px solid rgba(255,255,255,.8);color:var(--white);font-size:10.5px;font-weight:500;display:flex;align-items:center;justify-content:center}
.hero-craft{left:100px;top:152px;width:330px;height:346px;border-radius:40% 40% 30% 30%;background:radial-gradient(ellipse at 50% 45%,#e9eef2 0%,#b8c0c7 40%,#333b44 75%,rgba(20,30,40,0) 76%)}

/* Section labels */
.eyebrow{font-size:11px;color:var(--green);font-family:"Poppins",sans-serif}
.sec-title{font-family:"Poppins",sans-serif;font-weight:500;font-size:27px;color:var(--ink)}
.para{font-size:11.3px;line-height:18px;color:var(--body)}

/* Welcome */
.welcome .eyebrow{left:219px;top:580px}
.welcome .sec-title{left:219px;top:596px}
.welcome .col-a{left:219px;top:650px;width:340px}
.welcome .col-b{left:637px;top:650px;width:343px}

/* Services */
.services{position:absolute;left:0;top:806px;width:1200px;height:608px;overflow:hidden}
.services-photo{position:absolute;inset:0;background:linear-gradient(180deg,#0d2344 0%,#172c4a 45%,#3a1a1d 70%,#0a0d14 100%)}
.services-accent{position:absolute;left:70px;top:230px;width:1050px;height:170px;border-radius:50%;background:radial-gradient(ellipse at 50% 50%,rgba(200,30,30,.75) 0%,rgba(120,15,20,.5) 45%,rgba(0,0,0,0) 70%)}
.services .eyebrow{left:0;width:1200px;text-align:center;top:66px}
.services .sec-title{left:0;width:1200px;text-align:center;top:81px;color:var(--white)}
.services .lead{left:300px;top:129px;width:600px;text-align:center;color:#e6e9ee}
.services .tail{left:300px;top:473px;width:600px;text-align:center;color:#e6e9ee}
.grid{left:219px;top:234px;display:grid;grid-template-columns:repeat(4,181px);column-gap:14px;row-gap:15px}
.tile{height:53px;background:rgba(8,10,14,.86);display:flex;align-items:center;gap:12px;padding-left:12px;font-family:"Poppins",sans-serif;font-size:10.5px;line-height:13px;color:var(--white)}
.tile svg{flex:none}

/* Broadcast design */
.design .eyebrow{left:219px;top:1491px}
.design .sec-title{left:219px;top:1507px}
.design .para{left:219px;top:1553px;width:305px}
.proof{left:386px;top:1703px;width:108px;height:108px;border-radius:50%;background:var(--navy);border:5px solid var(--white);box-shadow:0 0 0 3px var(--navy);display:flex;align-items:center;justify-content:center;text-align:center;font-family:"Poppins",sans-serif;font-size:10px;font-weight:600;line-height:13px;color:var(--white)}
.flyer{border:4px solid #fff;box-shadow:0 6px 18px rgba(0,0,0,.35)}
.flyer-a{left:625px;top:1500px;width:212px;height:320px;transform:rotate(-9deg);background:linear-gradient(180deg,#f2f2f2 0 14%,#1a1a1a 14% 100%)}
.flyer-b{left:712px;top:1580px;width:230px;height:320px;transform:rotate(-9deg);background:linear-gradient(180deg,#0d1b33 0%,#24446e 55%,#0e1d35 100%)}

/* Pricing */
.pricing{position:absolute;left:0;top:1908px;width:1200px;height:675px;background:var(--navy-deep)}
.pricing .eyebrow{left:0;width:1200px;text-align:center;top:87px}
.pricing .sec-title{left:0;width:1200px;text-align:center;top:103px;color:var(--white)}
.card{top:190px;width:254px;height:409px;background:var(--white);box-shadow:0 10px 25px rgba(0,0,0,.35)}
.card.featured{top:169px;height:430px;z-index:2}
.card-head{height:62px;background:var(--navy-btn);color:var(--white);font-family:"Poppins",sans-serif;font-size:15px;display:flex;align-items:center;justify-content:center}
.card.featured .card-head{height:83px;background:var(--green);padding-top:20px}
.card-head b{font-weight:600;margin-left:5px}
.price{height:69px;background:var(--grey-band);display:flex;align-items:center;justify-content:center;font-family:"Poppins",sans-serif;font-weight:600;font-size:22px;color:var(--ink)}
.features{list-style:none;padding:16px 30px 0}
.features li{height:30px;border-bottom:1px solid #eeeeee;font-size:10.5px;color:var(--body);display:flex;align-items:center;justify-content:center}
.features li:last-child{border-bottom:none}
.card .btn{display:flex;align-items:center;justify-content:center;margin:10px auto 0;width:200px;height:38px;background:var(--navy-btn);color:var(--white);font-size:12px;font-weight:500}
.card.featured .btn{background:var(--green)}
.badge{left:552px;top:155px;width:98px;height:27px;border-radius:14px;background:#e31b1b;color:#fff;font-family:"Poppins",sans-serif;font-size:9.5px;font-weight:600;display:flex;align-items:center;justify-content:center;z-index:3}

/* Footer */
.footer{position:absolute;left:0;top:2583px;width:1200px;height:270px;background:var(--navy-deep);border-top:5px solid var(--green)}
.footer h4{font-size:11px;font-weight:600;color:var(--white);letter-spacing:.3px;white-space:nowrap}
.footer .col{top:58px}
.footer ul{list-style:none;margin-top:10px}
.footer li,.footer p{font-size:10.5px;line-height:17px;color:#aab4c3}
.mail-form{left:740px;top:84px;width:240px;height:30px;display:flex;background:var(--white)}
.mail-form span{flex:1;font-size:10.5px;color:#888;display:flex;align-items:center;padding-left:12px}
.mail-form b{width:80px;margin:3px;background:var(--green);color:#fff;font-family:"Poppins",sans-serif;font-size:10px;font-weight:600;display:flex;align-items:center;justify-content:center}
.social{left:740px;top:132px;display:flex;gap:9px}
.social i{width:23px;height:23px;background:#8b97a8}
.copyright{left:0;width:1200px;top:218px;text-align:center;font-size:10.5px;color:#8592a5}
</style>
</head>
<body>

<header class="hero">
  <svg class="hero-bg" width="1200" height="512" viewBox="0 0 1200 512" aria-hidden="true">
    <defs>
      <linearGradient id="skyGrad" x1="0" y1="1" x2="1" y2="0">
        <stop offset="0" stop-color="#4fa31c"/>
        <stop offset="0.35" stop-color="#1f5a4a"/>
        <stop offset="0.7" stop-color="#143656"/>
        <stop offset="1" stop-color="#0f2a4b"/>
      </linearGradient>
      <linearGradient id="waveGrad" x1="0" y1="0" x2="1" y2="1">
        <stop offset="0" stop-color="#4ea51a"/>
        <stop offset="1" stop-color="#67bd1f"/>
      </linearGradient>
    </defs>
    <rect width="1200" height="512" fill="url(#skyGrad)"/>
    <path d="M0,190 C260,250 420,420 600,512 L0,512 Z" fill="url(#waveGrad)"/>
    <path d="M600,512 C820,450 1020,370 1200,285 L1200,512 Z" fill="url(#waveGrad)"/>
    <path d="M0,300 C180,360 360,470 600,512 L0,512 Z" fill="#ffffff"/>
    <path d="M600,512 C820,450 1020,370 1200,285" fill="none" stroke="#ffffff" stroke-width="2"/>
  </svg>
  <div class="abs hero-craft" role="img" aria-label="Photo of a white light helicopter in flight, front three-quarter view"></div>
  <div class="abs logo"><span class="dot"></span>Rotorline Parade</div>
  <nav class="abs nav">
    <a class="active">Home</a><a>Services</a><a>Broadcast Design</a><a>Pricing</a><a>Contact</a>
  </nav>
  <div class="abs phone">
    <svg width="12" height="12" viewBox="0 0 24 24" aria-hidden="true"><path fill="#fff" d="M6.6 10.8a15.1 15.1 0 0 0 6.6 6.6l2.2-2.2a1 1 0 0 1 1-.25 11.4 11.4 0 0 0 3.6.57 1 1 0 0 1 1 1V20a1 1 0 0 1-1 1A17 17 0 0 1 3 4a1 1 0 0 1 1-1h3.5a1 1 0 0 1 1 1c0 1.25.2 2.45.57 3.57a1 1 0 0 1-.25 1z"/></svg>
    1800 555 014
  </div>
  <div class="abs btn btn-subscribe">SUBSCRIBE</div>
  <h1 class="abs hero-title">Exclusively Showcasing Rotor Wing Aircraft to the Global Marketplace</h1>
  <div class="abs btn btn-outline">CONTACT US TODAY</div>
</header>

<section class="welcome">
  <div class="abs eyebrow">Welcome</div>
  <h2 class="abs sec-title">Rotorline Parade</h2>
  <p class="abs para col-a">Rotorline Parade is one of most powerful marketing tools in the industry to utilize in reaching targeted buyers of pre-owned helicopters. Rotorline Parade provides the rotor wing aircraft market with a fast, effective, and affordable email broadcast solution to utilize in the marketing of Helicopters for sale.</p>
  <p class="abs para col-b">Developed Exclusively to Parade Rotor Wing Aircraft to the Global marketplace, Rotorline Parade is a powerful tool designed to maximize leads and accelerate the sales process by providing the ability to reach a global network of Helicopter buyers in a matter of seconds.</p>
</section>

<section class="services">
  <div class="services-photo" role="img" aria-label="Night photo of a red and black helicopter parked on a tarmac under a dusk sky"></div>
  <div class="services-accent" aria-hidden="true"></div>
  <div class="abs eyebrow">Rotorline Parade</div>
  <h2 class="abs sec-title">Services Offer</h2>
  <p class="abs para lead">Rotorline Parade is one of most powerful marketing tools in the industry to utilize in reaching targeted buyers of pre-owned helicopters. Rotorline Parade provides the rotor wing aircraft market with a fast, effective, and affordable email broadcast solution to utilize in the marketing of Helicopters for sale.</p>
  <div class="abs grid">
    <div class="tile"><svg width="20" height="20" viewBox="0 0 20 20" aria-hidden="true"><circle cx="10" cy="10" r="9" fill="none" stroke="#5cb31a" stroke-width="1.5"/><path d="M5 8h10M10 8v6M7 14h6" stroke="#5cb31a" stroke-width="1.5"/></svg>Helicopter Owners</div>
    <div class="tile"><svg width="20" height="20" viewBox="0 0 20 20" aria-hidden="true"><circle cx="10" cy="10" r="9" fill="none" stroke="#5cb31a" stroke-width="1.5"/><path d="M5 8h10M10 8v6M7 14h6" stroke="#5cb31a" stroke-width="1.5"/></svg>Helicopter Operators</div>
    <div class="tile"><svg width="20" height="20" viewBox="0 0 20 20" aria-hidden="true"><circle cx="10" cy="10" r="9" fill="none" stroke="#5cb31a" stroke-width="1.5"/><path d="M5 8h10M10 8v6M7 14h6" stroke="#5cb31a" stroke-width="1.5"/></svg>Helicopter Charter<br>Services</div>
    <div class="tile"><svg width="20" height="20" viewBox="0 0 20 20" aria-hidden="true"><circle cx="10" cy="10" r="9" fill="none" stroke="#5cb31a" stroke-width="1.5"/><path d="M5 8h10M10 8v6M7 14h6" stroke="#5cb31a" stroke-width="1.5"/></svg>Municipalities/Media<br>/Medevac Firms</div>
    <div class="tile"><svg width="20" height="20" viewBox="0 0 20 20" aria-hidden="true"><circle cx="10" cy="10" r="9" fill="none" stroke="#5cb31a" stroke-width="1.5"/><path d="M5 8h10M10 8v6M7 14h6" stroke="#5cb31a" stroke-width="1.5"/></svg>Corporate/Municipal<br>Flight Departments</div>
    <div class="tile"><svg width="20" height="20" viewBox="0 0 20 20" aria-hidden="true"><circle cx="10" cy="10" r="9" fill="none" stroke="#5cb31a" stroke-width="1.5"/><path d="M5 8h10M10 8v6M7 14h6" stroke="#5cb31a" stroke-width="1.5"/></svg>Helicopter Pilots</div>
    <div class="tile"><svg width="20" height="20" viewBox="0 0 20 20" aria-hidden="true"><circle cx="10" cy="10" r="9" fill="none" stroke="#5cb31a" stroke-width="1.5"/><path d="M5 8h10M10 8v6M7 14h6" stroke="#5cb31a" stroke-width="1.5"/></svg>Senior Aviation<br>Executives</div>
    <div class="tile"><svg width="20" height="20" viewBox="0 0 20 20" aria-hidden="true"><circle cx="10" cy="10" r="9" fill="none" stroke="#5cb31a" stroke-width="1.5"/><path d="M5 8h10M10 8v6M7 14h6" stroke="#5cb31a" stroke-width="1.5"/></svg>Wealth Management<br>Firms</div>
    <div class="tile"><svg width="20" height="20" viewBox="0 0 20 20" aria-hidden="true"><circle cx="10" cy="10" r="9" fill="none" stroke="#5cb31a" stroke-width="1.5"/><path d="M5 8h10M10 8v6M7 14h6" stroke="#5cb31a" stroke-width="1.5"/></svg>High Net Worth<br>Individuals</div>
    <div class="tile"><svg width="20" height="20" viewBox="0 0 20 20" aria-hidden="true"><circle cx="10" cy="10" r="9" fill="none" stroke="#5cb31a" stroke-width="1.5"/><path d="M5 8h10M10 8v6M7 14h6" stroke="#5cb31a" stroke-width="1.5"/></svg>Helicopter<br>Broker/Dealers</div>
    <div class="tile"><svg width="20" height="20" viewBox="0 0 20 20" aria-hidden="true"><circle cx="10" cy="10" r="9" fill="none" stroke="#5cb31a" stroke-width="1.5"/><path d="M5 8h10M10 8v6M7 14h6" stroke="#5cb31a" stroke-width="1.5"/></svg>Helicopter Tour/<br>Travel Firms</div>
    <div class="tile"><svg width="20" height="20" viewBox="0 0 20 20" aria-hidden="true"><circle cx="10" cy="10" r="9" fill="none" stroke="#5cb31a" stroke-width="1.5"/><path d="M5 8h10M10 8v6M7 14h6" stroke="#5cb31a" stroke-width="1.5"/></svg>Off Shore Oil &amp; Gas<br>Production Firms</div>
  </div>
  <p class="abs para tail">Rotorline Parade is one of most powerful marketing tools in the industry to utilize in reaching targeted buyers of pre-owned helicopters. Rotorline Parade provides the rotor wing aircraft market with a fast, effective, and affordable email broadcast solution to utilize in the marketing of Helicopters for sale.</p>
</section>

<section class="design">
  <svg class="abs" style="left:0;top:1500px" width="1200" height="410" viewBox="0 0 1200 410" aria-hidden="true">
    <path d="M0,402 L1200,12 L1200,145 L0,408 Z" fill="#5cb31a"/>
  </svg>
  <div class="abs eyebrow">Rotorline Parade</div>
  <h2 class="abs sec-title">Brodcast Design</h2>
  <p class="abs para">Rotorline Parade is one of most powerful marketing tools in the industry to utilize in reaching targeted buyers of pre-owned helicopters. Rotorline Parade provides the rotor wing aircraft market with a fast, effective, and affordable email broadcast solution to utilize in the marketing of Helicopters for sale.</p>
  <div class="abs proof">RECEIVE A<br>DESIGN PROOF</div>
  <div class="abs flyer flyer-a" role="img" aria-label="Sample broadcast flyer advertising a pre-owned helicopter for sale"></div>
  <div class="abs flyer flyer-b" role="img" aria-label="Sample broadcast flyer for a helicopter wanted for acquisition"></div>
</section>

<section class="pricing">
  <div class="abs eyebrow">3 Different Rotorline Parade</div>
  <h2 class="abs sec-title">Broadcast Packages</h2>
  <div class="abs badge">MOST POPULAR</div>

  <div class="abs card" style="left:220px">
    <div class="card-head">Broadcast <b>Package A</b></div>
    <div class="price">$39.99</div>
    <ul class="features">
      <li>01. Awesome lorem ipsum dolor sit</li><li>02. Awesome lorem ipsum dolor sit</li><li>03. Awesome lorem ipsum dolor sit</li>
      <li>04. Awesome lorem ipsum dolor sit</li><li>05. Awesome lorem ipsum dolor sit</li><li>06. Awesome lorem ipsum dolor sit</li>
    </ul>
    <div class="btn">SELECT PACKAGE</div>
  </div>

  <div class="abs card featured" style="left:474px">
    <div class="card-head">Broadcast <b>Package B</b></div>
    <div class="price">$39.99</div>
    <ul class="features">
      <li>01. Awesome lorem ipsum dolor sit</li><li>02. Awesome lorem ipsum dolor sit</li><li>03. Awesome lorem ipsum dolor sit</li>
      <li>04. Awesome lorem ipsum dolor sit</li><li>05. Awesome lorem ipsum dolor sit</li><li>06. Awesome lorem ipsum dolor sit</li>
    </ul>
    <div class="btn">SELECT PACKAGE</div>
  </div>

  <div class="abs card" style="left:728px">
    <div class="card-head">Broadcast <b>Package C</b></div>
    <div class="price">$39.99</div>
    <ul class="features">
      <li>01. Awesome lorem ipsum dolor sit</li><li>02. Awesome lorem ipsum dolor sit</li><li>03. Awesome lorem ipsum dolor sit</li>
      <li>04. Awesome lorem ipsum dolor sit</li><li>05. Awesome lorem ipsum dolor sit</li><li>06. Awesome lorem ipsum dolor sit</li>
    </ul>
    <div class="btn">SELECT PACKAGE</div>
  </div>
</section>

<footer class="footer">
  <div class="abs col" style="left:219px">
    <h4>CONTACT INFO</h4>
    <p style="margin-top:10px">228, lorem ipsum dolor,<br>dosis amet - 45895</p>
    <p style="margin-top:17px">T: 1800 555 0147<br>E: info@rotorlineparade.com</p>
  </div>
  <div class="abs col" style="left:428px">
    <h4>QUICK LINKS</h4>
    <ul><li>Home</li><li>Services</li><li>Broadcast Design</li><li>Pricing</li><li>Contact</li></ul>
  </div>
  <div class="abs col" style="left:590px">
    <h4>HELPFUL LINKS</h4>
    <ul><li>Terms of Use</li><li>Privacy Policy</li><li>Sitemap</li><li>Contact Us</li></ul>
  </div>
  <div class="abs col" style="left:740px">
    <h4>SUBSCRIBE TO JOIN OUR MAILING LIST</h4>
  </div>
  <div class="abs mail-form"><span>Email Address</span><b>SUBSCRIBE</b></div>
  <div class="abs social" aria-label="Social links"><i></i><i></i><i></i><i></i></div>
  <p class="abs copyright">Copyright © 2018 Rotorline Parade. All Rights Reserved</p>
</footer>

</body>
</html>
```